KBRF website design

We need a page template website design for a cms website. Please see the brief attached for the details.
The client is the Kestrel Brook Ramfold Federation which is an organisation promoting the KBRF Sheep Breed within Australia.
Updates

Reason: So that my top few designs can make changes and re-submit.

Target Market(s)

See attached brief

```html
<!DOCTYPE html>
<html lang="en">
<head>
<meta charset="utf-8">
<title>KBRF – Home</title>
<link href="https://fonts.googleapis.com/css2?family=Arvo:wght@400&family=Open+Sans:wght@400;600;700&display=swap" rel="stylesheet">
<style>
:root{
  --green:#0f9a4a;
  --green-dark:#0b8640;
  --green-light:#16a955;
  --yellow:#f8c628;
  --text:#666666;
  --heading:#128f48;
  --footer:#2e2e2e;
  --white:#ffffff;
  --frame-shadow:rgba(0,0,0,.22);
}
*{box-sizing:border-box;margin:0;padding:0}
html,body{width:1036px;height:1200px;overflow:hidden}
body{position:relative;background:var(--white);font-family:"Open Sans",Arial,sans-serif;color:var(--text)}
.site-header{position:absolute;left:0;top:0;width:1036px;height:160px;background:linear-gradient(#ffffff,#f3f3f3)}
.brand-mark{position:absolute;left:78px;top:28px;display:flex;align-items:center;gap:12px}
.brand-mark .dot{width:54px;height:54px;border-radius:50%;background:var(--green)}
.brand-mark .name{font-family:"Open Sans",Arial,sans-serif;font-weight:700;font-size:38px;color:var(--green)}
.org-title{position:absolute;left:336px;top:44px;font-family:"Arvo",Georgia,serif;font-size:25px;line-height:40px;color:var(--heading);letter-spacing:.3px}
.search{position:absolute;left:737px;top:66px;width:225px;height:30px;border:1px solid #d3d3d3;background:var(--white);font-size:12px;color:#888;padding:6px 11px}
.search svg{position:absolute;right:8px;top:8px}
.main-nav{position:absolute;left:0;top:160px;width:1036px;height:50px;background:linear-gradient(var(--green-light),var(--green-dark))}
.main-nav ul{list-style:none;display:flex;position:absolute;left:75px;top:0;height:50px}
.main-nav li{height:50px;line-height:50px;padding:0 19px;font-weight:700;font-size:14px;color:var(--white);text-shadow:0 1px 1px rgba(0,0,0,.35);border-right:1px solid rgba(0,0,0,.12);letter-spacing:-.2px}
.main-nav li.active{background:var(--yellow);padding:0 20px}
.slider{position:absolute;left:75px;top:230px;width:886px;height:300px;background:var(--white);box-shadow:0 1px 5px var(--frame-shadow)}
.slide-photo{position:absolute;left:8px;top:8px;width:870px;height:284px;background:linear-gradient(#b9c6d3 0%,#7d8b72 28%,#4f6a3c 50%,#6f9a45 72%,#5d8d38 100%)}
.slide-caption{position:absolute;left:8px;top:151px;height:52px;padding:0 17px;background:rgba(40,40,40,.55);color:var(--white);font-weight:600;font-size:25px;line-height:52px;letter-spacing:.2px}
.dots{position:absolute;left:476px;top:269px;display:flex;gap:4px}
.dots span{width:15px;height:15px;border-radius:50%;background:rgba(255,255,255,.6)}
.dots span.on{background:var(--white)}
.feature{position:absolute;top:590px;width:189px;height:122px;background:var(--white);box-shadow:0 1px 5px var(--frame-shadow)}
.feature .pic{position:absolute;left:4px;top:4px;width:181px;height:114px}
.feature .label{position:absolute;left:4px;top:92px;width:181px;height:26px;background:rgba(40,40,40,.6);color:var(--white);font-weight:600;font-size:13px;line-height:26px;padding-left:7px}
.welcome{position:absolute;left:74px;top:768px;width:530px}
h2{font-weight:400;font-size:23px;color:var(--heading);line-height:30px}
.welcome p{font-size:12.4px;line-height:22.5px;margin-top:14px;word-break:break-all}
.welcome h2+p{margin-top:16px}
.sponsors{position:absolute;left:662px;top:768px;width:299px}
.arrows{position:absolute;right:2px;top:7px;display:flex;gap:7px}
.arrows span{width:20px;height:20px;background:#7d7d7d;display:block}
.sponsor-ad{position:absolute;left:7px;top:52px;width:290px;height:219px;background:linear-gradient(#dccbcb,#d7c6c6)}
.site-footer{position:absolute;left:0;top:1095px;width:1036px;height:105px;background:var(--footer);font-family:Arial,Helvetica,sans-serif;color:var(--white)}
.footer-links{position:absolute;left:75px;top:29px;font-size:12.5px}
.copyright{position:absolute;left:75px;top:61px;font-size:12.5px}
.social{position:absolute;left:774px;top:38px;display:flex;gap:10px}
.social span{width:31px;height:31px;display:block}
</style>
</head>
<body>
<header class="site-header">
  <div class="brand-mark"><span class="dot"></span><span class="name">KBRF</span></div>
  <div class="org-title">KESTREL BROOK RAMFOLD<br>FEDERATION</div>
  <div class="search">Search..
    <svg width="12" height="12" viewBox="0 0 12 12"><circle cx="5" cy="5" r="3.8" fill="none" stroke="#999" stroke-width="1.6"/><line x1="7.8" y1="7.8" x2="11" y2="11" stroke="#999" stroke-width="1.8"/></svg>
  </div>
</header>
<nav class="main-nav">
  <ul>
    <li class="active">HOME</li><li>ABOUT</li><li>SEARCH</li><li>MEMBER SERVICES</li><li>STUD PAGES</li><li>NEWS</li><li>SALES</li><li>LINKS</li><li>CONTACT</li>
  </ul>
</nav>
<section class="slider">
  <div class="slide-photo" role="img" aria-label="Flock of white sheep grazing in a green paddock below wooded hills"></div>
  <div class="slide-caption">PROIN GRAVIDA NIBH VEL VELIT</div>
  <div class="dots"><span class="on"></span><span></span><span></span><span></span></div>
</section>
<div class="feature" style="left:75px"><div class="pic" role="img" aria-label="Sheep in front of a hill" style="background:linear-gradient(#a9b7c6,#7d7a6a 55%,#8a6d4c)"></div><div class="label">Prime Lamb Helpline</div></div>
<div class="feature" style="left:309px"><div class="pic" role="img" aria-label="Calendar page with pins" style="background:linear-gradient(135deg,#f2f2f2,#c9c9c9)"></div><div class="label">Events</div></div>
<div class="feature" style="left:541px"><div class="pic" role="img" aria-label="Group of members in business attire" style="background:linear-gradient(#e9e9e9,#7a7a7a 60%,#3a3a3a)"></div><div class="label">Members</div></div>
<div class="feature" style="left:773px"><div class="pic" role="img" aria-label="Close-up of farm equipment" style="background:linear-gradient(135deg,#7a4a3a,#c9b8ae 50%,#5e3a2e)"></div><div class="label">Latest News</div></div>
<section class="welcome">
  <h2>Welcome to our website</h2>
  <p>Mirum est notare quam littera gothica, quam nunc putamus parum claram, anteposuerit litterarum formas humanitatis per seacula quarta decima et quinta decima. &nbsp;Nam liber tempor cum soluta nobis eleifend option congue nihil imperdiet doming id quod mazim placerat facer possim assum. Typi non habent claritatem insitam; est usus legentis in iis qiui facit eorum claritatem. Investigationes demonstraverunt lectores legere me lius.</p>
  <p>Nam liber tempor cum soluta nobis eleifend option conngue nhil imperdiet doming id quiod mazim placerat facer possim assum. Typi non habent claritatem insitam; est usus legentis in iis qui facit eorum claritatem. Investigationes demonstraverunt lectores legere me lius quod ii legunt saepius. Claritas est etiam processus dynamicus, qui sequitur mutationem consuetudium lectorum. Mirum est notare quam littera gothica</p>
</section>
<aside class="sponsors">
  <h2>Sponsers</h2>
  <div class="arrows">
    <span><svg width="20" height="20" viewBox="0 0 20 20"><polyline points="12,5 7,10 12,15" fill="none" stroke="#fff" stroke-width="1.5"/></svg></span>
    <span><svg width="20" height="20" viewBox="0 0 20 20"><polyline points="8,5 13,10 8,15" fill="none" stroke="#fff" stroke-width="1.5"/></svg></span>
  </div>
  <div class="sponsor-ad" role="img" aria-label="Sponsor advertisement for Ironbark Cattle Co with a photo of a bull"></div>
</aside>
<footer class="site-footer">
  <div class="footer-links">Home | About | Search | Member Services | Stud Pages | News | Sales | Links | Contact</div>
  <div class="copyright">Copyright © 2013. All Rights Reserved.</div>
  <div class="social">
    <span style="background:#3b5ba6" role="img" aria-label="Social link"></span>
    <span style="background:#2fa4dc" role="img" aria-label="Social link"></span>
    <span style="background:#f0711f" role="img" aria-label="Feed link"></span>
    <span style="background:#e0262c" role="img" aria-label="Video link"></span>
  </div>
</footer>
</body>
</html>
```